Local jobs for students, local vendor post jobs, register users (students) receive notification

I need a simple app design for local shops to post jobs, register users (students) will then receive notifications base on their location (district...)

University students and local shops (flower, coffee, restaurant, etc.)

• Open up app:
• Page 1: Show 2 buttons: View recent jobs and Post a New Jobs
• Login/Registration pages
• Page 2: User registration (Name, Email, Phone and Login with Lumora)
• Page 3: User selection - Students or Local Shops
• Page 3a: If students - fill in the school name, select city, select districts that able to work, maximum 3 selection.
• Page 3b: If local shops - fill in the business name, select the business type (flower, coffee, restaurants, etc.), upload shop image, minimum 1 image maximum 3 images.
• Page 4a: Complete registration - View jobs button if student
• Page 4b: Complete registration - View post job button if vendors
• Signed in pages:
• On click view jobs button:
• Page 5a - Student - List of recent jobs (posted within 48 hours) with premium job display on top, list by most recent, small image of shop, short description, 3 lines of text, click an item to view more.
• Once click on item, show full contents (75 words maximum) with images, and a CALL NOW BUTTON
• On click post jobs button:
• Page 5b - Post job page - input job description in 50 words, select post type (free or premium)
• If premium select, payment type drop-down: show the description of the premium post (3 lines of texts), Credit Card payment inputs.
• Proceed to payment verification:
• Preview Post - Submit button
• DESIGN
• Font - Proxima Nova, Open Sans, Roboto (Unikey friendly, as the app will be in Vietnamese, will provide translation later)
• Style - Flat, Clean
• Color - Bold

```html
<!DOCTYPE html>
<html lang="en">
<head>
<meta charset="utf-8">
<title>Recent Jobs</title>
<link rel="stylesheet" href="https://fonts.googleapis.com/css2?family=Roboto:wght@400;500&display=swap">
<style>
  :root {
    --page-bg: #d6e3ef;
    --brand-blue: #2f8ad6;
    --on-brand: #ffffff;
    --band-bg: #e4e4e4;
    --band-text: #3a3a3a;
    --list-bg: #f1f1f1;
    --card-bg: #ffffff;
    --card-shadow: rgba(0, 0, 0, 0.10);
    --title-text: #333333;
    --body-text: #6f6f6f;
    --meta-text: #7a7a7a;
  }
  * { box-sizing: border-box; margin: 0; padding: 0; }
  html, body {
    width: 1200px;
    height: 1200px;
    overflow: hidden;
    background: var(--page-bg);
    font-family: "Roboto", Arial, sans-serif;
  }
  .app-screen {
    position: absolute;
    left: 276px;
    top: 20px;
    width: 648px;
    height: 1160px;
    background: var(--list-bg);
    overflow: hidden;
    box-shadow: 0 20px 50px rgba(60, 90, 120, 0.25);
  }
  .status-bar {
    height: 47px;
    background: var(--brand-blue);
    color: var(--on-brand);
    display: flex;
    align-items: center;
    justify-content: space-between;
    padding: 0 10px 0 10px;
    font-size: 19px;
    position: relative;
  }
  .status-left, .status-right { display: flex; align-items: center; gap: 7px; }
  .signal { display: flex; gap: 2px; }
  .signal span {
    width: 9px; height: 9px; border-radius: 50%;
    border: 1.5px solid var(--on-brand);
  }
  .signal span.on { background: var(--on-brand); }
  .status-time {
    position: absolute; left: 0; right: 0; text-align: center;
    pointer-events: none;
  }
  .battery {
    width: 40px; height: 16px; border: 1.5px solid var(--on-brand);
    border-radius: 3px; padding: 2px; position: relative;
  }
  .battery::before {
    content: ""; display: block; width: 100%; height: 100%;
    background: var(--on-brand); border-radius: 1px;
  }
  .battery::after {
    content: ""; position: absolute; right: -5px; top: 4px;
    width: 3px; height: 6px; background: var(--on-brand); border-radius: 0 2px 2px 0;
  }
  .nav-bar {
    height: 68px;
    background: var(--brand-blue);
    color: var(--on-brand);
    display: flex;
    align-items: center;
    justify-content: space-between;
    padding: 0 16px 0 14px;
  }
  .nav-title { font-size: 26px; font-weight: 500; }
  .location-band {
    height: 53px;
    background: var(--band-bg);
    color: var(--band-text);
    display: flex;
    align-items: center;
    justify-content: center;
    font-size: 22px;
    letter-spacing: 0.2px;
  }
  .job-list {
    list-style: none;
    padding: 15px 15px 0 15px;
  }
  .job-card {
    height: 132px;
    margin-bottom: 12px;
    background: var(--card-bg);
    box-shadow: 0 2px 3px var(--card-shadow);
    position: relative;
    display: flex;
  }
  .shop-photo {
    position: absolute;
    left: 11px; top: 9px;
    width: 121px; height: 112px;
  }
  .job-text {
    position: absolute;
    left: 148px; top: 22px; right: 14px;
  }
  .job-title {
    font-size: 19px; font-weight: 500; color: var(--title-text);
    text-transform: uppercase; letter-spacing: 0.1px;
  }
  .job-summary {
    margin-top: 10px;
    font-size: 19px; line-height: 27px; color: var(--body-text);
  }
  .job-age {
    position: absolute; right: 14px; top: 25px;
    font-size: 15px; color: var(--meta-text);
  }
  .photo-1 { background: linear-gradient(135deg, #4b4a52, #8a6b55 55%, #c8a487); }
  .photo-2 { background: linear-gradient(135deg, #6b4a3a, #a85b6a 50%, #7a9a5a); }
  .photo-3 { background: linear-gradient(135deg, #3c4a34, #8aa062 50%, #d4a0a8); }
  .photo-4 { background: linear-gradient(180deg, #b8e0dc, #6a5a48 45%, #4f8a3a 75%, #3a2a22); }
  .photo-5 { background: linear-gradient(135deg, #6a3aa8, #9a6ad0 50%, #4a4a5a); }
  .photo-6 { background: linear-gradient(180deg, #8a7a5a, #c8b89a 50%, #6a5040); }
  .photo-7 { background: linear-gradient(180deg, #3a6a3a, #5a8a9a 50%, #2a4a8a); }
</style>
</head>
<body>
  <main class="app-screen">
    <header>
      <div class="status-bar">
        <div class="status-left">
          <div class="signal"><span class="on"></span><span class="on"></span><span class="on"></span><span></span><span></span></div>
          <span class="carrier">NOVA</span>
          <svg width="20" height="16" viewBox="0 0 20 16" aria-hidden="true">
            <path d="M1 5.5a13 13 0 0 1 18 0" fill="none" stroke="#fff" stroke-width="2" stroke-linecap="round"/>
            <path d="M4.2 8.8a8.5 8.5 0 0 1 11.6 0" fill="none" stroke="#fff" stroke-width="2" stroke-linecap="round"/>
            <path d="M10 15l-3-3.2a4.2 4.2 0 0 1 6 0z" fill="#fff"/>
          </svg>
        </div>
        <div class="status-time">4:21 PM</div>
        <div class="status-right">
          <svg width="12" height="20" viewBox="0 0 12 20" aria-hidden="true">
            <path d="M1 6l9 8-4.5 4V2L10 6l-9 8" fill="none" stroke="#fff" stroke-opacity="0.8" stroke-width="1.5" stroke-linejoin="round"/>
          </svg>
          <span>100%</span>
          <div class="battery"></div>
        </div>
      </div>
      <nav class="nav-bar">
        <svg width="32" height="24" viewBox="0 0 32 24" aria-label="Back">
          <path d="M30 12H3M13 2L3 12l10 10" fill="none" stroke="#fff" stroke-width="2.4" stroke-linecap="round" stroke-linejoin="round"/>
        </svg>
        <h1 class="nav-title">Recent Jobs</h1>
        <svg width="26" height="28" viewBox="0 0 26 28" aria-label="Filter">
          <path d="M1 1h24l-9 12v13l-6-3V13z" fill="#fff"/>
        </svg>
      </nav>
    </header>

    <div class="location-band">HOCHIMINH CITY - PHU NHUAN DIST</div>

    <ul class="job-list">
      <li class="job-card">
        <div class="shop-photo photo-1" role="img" aria-label="Photo of a street food stall front"></div>
        <div class="job-text">
          <h2 class="job-title">Lorem ipsum dolor sit amet.</h2>
          <p class="job-summary">Lorem ipsum dolor sit amet, consectetur adipiscing elit. Etiam vitae eros efficitur finibus.</p>
        </div>
        <span class="job-age">15 min</span>
      </li>
      <li class="job-card">
        <div class="shop-photo photo-2" role="img" aria-label="Photo of a flower shop front with bouquets"></div>
        <div class="job-text">
          <h2 class="job-title">Lorem ipsum dolor sit amet.</h2>
          <p class="job-summary">Lorem ipsum dolor sit amet, consectetur adipiscing elit. Etiam vitae eros efficitur finibus.</p>
        </div>
        <span class="job-age">30 min</span>
      </li>
      <li class="job-card">
        <div class="shop-photo photo-3" role="img" aria-label="Photo of a florist storefront on a street"></div>
        <div class="job-text">
          <h2 class="job-title">Lorem ipsum dolor sit amet.</h2>
          <p class="job-summary">Lorem ipsum dolor sit amet, consectetur adipiscing elit. Etiam vitae eros efficitur finibus.</p>
        </div>
        <span class="job-age">1 hou</span>
      </li>
      <li class="job-card">
        <div class="shop-photo photo-4" role="img" aria-label="Photo of a small cafe with an awning and stools"></div>
        <div class="job-text">
          <h2 class="job-title">Lorem ipsum dolor sit amet.</h2>
          <p class="job-summary">Lorem ipsum dolor sit amet, consectetur adipiscing elit. Etiam vitae eros efficitur finibus.</p>
        </div>
        <span class="job-age">2 hou</span>
      </li>
      <li class="job-card">
        <div class="shop-photo photo-5" role="img" aria-label="Photo of a purple painted cafe front"></div>
        <div class="job-text">
          <h2 class="job-title">Lorem ipsum dolor sit amet.</h2>
          <p class="job-summary">Lorem ipsum dolor sit amet, consectetur adipiscing elit. Etiam vitae eros efficitur finibus.</p>
        </div>
        <span class="job-age">3 hou</span>
      </li>
      <li class="job-card">
        <div class="shop-photo photo-6" role="img" aria-label="Photo of a restaurant terrace with tables"></div>
        <div class="job-text">
          <h2 class="job-title">Lorem ipsum dolor sit amet.</h2>
          <p class="job-summary">Lorem ipsum dolor sit amet, consectetur adipiscing elit. Etiam vitae eros efficitur finibus.</p>
        </div>
        <span class="job-age">6 hou</span>
      </li>
      <li class="job-card">
        <div class="shop-photo photo-7" role="img" aria-label="Photo of a garden restaurant with blue chairs"></div>
        <div class="job-text">
          <h2 class="job-title">Lorem ipsum dolor sit amet.</h2>
          <p class="job-summary">Lorem ipsum dolor sit amet, consectetur adipiscing elit. Etiam vitae eros efficitur finibus.</p>
        </div>
        <span class="job-age">10 hou</span>
      </li>
    </ul>
  </main>
</body>
</html>
```